Australian Civil Construction, Quarry & Mining Services needs a business card

We need a business card designed for our Civil Construction, Quarry & Mining Services based in the country in Australia.
Our Company Brackley Earthworks provide innovate solutions for infrastructure, agricultural and mining (aggregate, sand, roadbase) industry.
We would like our business cards to be double sided
Front of card: black background or something that resembles our business colours. (it doesn't have to be black we are open to options)
- Company name - Brackley Earthworks
- Either our logo or some sort of icon/picture that resembles our business
- Website - https://brackleyearthworks.com.au/
- We will have a number of different names, positions descriptions, phone numbers and emails on separate cards for each of our managers/directors

```html
<!DOCTYPE html>
<html lang="en">
<head>
<meta charset="utf-8">
<title>Brackley Earthworks – Business Card</title>
<link rel="stylesheet" href="https://fonts.googleapis.com/css2?family=Arimo:wght@400;700&family=Exo+2:wght@700&display=swap">
<style>
  :root {
    --bg: #1d1d1d;
    --card-white: #f2f2f2;
    --brand-orange: #fb8217;
    --ink: #1a1718;
    --divider: #d4d4d4;
  }
  * { box-sizing: border-box; margin: 0; padding: 0; }
  html, body {
    width: 1200px;
    height: 900px;
    overflow: hidden;
    background: var(--bg);
    font-family: "Arimo", Arial, sans-serif;
  }
  .canvas { position: relative; width: 1200px; height: 900px; }

  .card {
    position: absolute;
    width: 560px;
    height: 320px;
  }

  /* Front: contact side */
  .card-front {
    left: 80px;
    top: 480px;
    background: var(--card-white);
    display: flex;
  }
  .brand-panel {
    width: 236px;
    display: flex;
    flex-direction: column;
    align-items: center;
    justify-content: center;
    gap: 18px;
    border-right: 1px solid var(--divider);
    margin: 40px 0;
  }
  .brand-dot {
    width: 96px;
    height: 96px;
    border-radius: 50%;
    background: var(--ink);
  }
  .brand-name {
    font-weight: 700;
    font-size: 17px;
    color: var(--brand-orange);
    letter-spacing: 0.5px;
  }
  .contact-panel {
    flex: 1;
    padding: 78px 0 0 30px;
  }
  .person-name {
    font-family: "Exo 2", "Arimo", sans-serif;
    font-weight: 700;
    font-size: 27px;
    color: var(--brand-orange);
    text-transform: uppercase;
    line-height: 1;
  }
  .person-role {
    font-size: 17px;
    color: var(--ink);
    margin-top: 4px;
  }
  .contact-list {
    list-style: none;
    margin-top: 26px;
  }
  .contact-item {
    display: flex;
    align-items: center;
    gap: 9px;
    font-size: 17px;
    color: var(--ink);
    line-height: 1.5;
  }
  .contact-icon { width: 16px; height: 16px; flex: none; }

  /* Back: brand side */
  .card-back {
    left: 560px;
    top: 100px;
    background: var(--brand-orange);
    display: flex;
    align-items: center;
    justify-content: center;
    gap: 20px;
  }
  .card-back .brand-dot { width: 130px; height: 130px; }
  .card-back .brand-name { color: var(--ink); font-size: 24px; }
</style>
</head>
<body>
<main class="canvas">

  <section class="card card-back" aria-label="Card back">
    <div class="brand-dot"></div>
    <span class="brand-name">Brackley Earthworks</span>
  </section>

  <section class="card card-front" aria-label="Card front">
    <div class="brand-panel">
      <div class="brand-dot"></div>
      <span class="brand-name">Brackley Earthworks</span>
    </div>
    <div class="contact-panel">
      <h1 class="person-name">Daniel Mercer</h1>
      <p class="person-role">Managing Director</p>
      <ul class="contact-list">
        <li class="contact-item">
          <svg class="contact-icon" viewBox="0 0 16 16" aria-hidden="true">
            <path d="M3.5 1.5l2.5 3-1.6 1.6c.8 1.8 2.2 3.2 4 4l1.6-1.6 3 2.5-1.5 2.5C7 13.5 2.5 9 1 4.5z" fill="var(--brand-orange)"/>
          </svg>
          044-555 010 234
        </li>
        <li class="contact-item">
          <svg class="contact-icon" viewBox="0 0 16 16" aria-hidden="true">
            <rect x="1" y="3" width="14" height="10" fill="var(--brand-orange)"/>
            <path d="M1 3l7 5.5L15 3" fill="none" stroke="var(--card-white)" stroke-width="1.3"/>
          </svg>
          info@brackleyearth.com
        </li>
        <li class="contact-item">
          <svg class="contact-icon" viewBox="0 0 16 16" aria-hidden="true">
            <g fill="none" stroke="var(--brand-orange)" stroke-width="1.4">
              <circle cx="8" cy="8" r="6.5"/>
              <ellipse cx="8" cy="8" rx="3" ry="6.5"/>
              <path d="M1.5 8h13M2.5 4.8h11M2.5 11.2h11"/>
            </g>
          </svg>
          www.brackleyearthworks.com.au
        </li>
      </ul>
    </div>
  </section>

</main>
</body>
</html>
```